Top Real Estate teams new cards UPDATED

New Cards with MY (Im the tall guy in the middle) new pic on the front of card and my team pic on the back of card. Also my team name on the front of the card (marlow and partners) and brokerage name on the back (harborline real estate group) . Also the tag line "Ask about our 20 step plan" on the back of the card and "Welcome to the new way of Real Estate Sales" on the front of the card along with my phone number (951-284-7310) and email address (devon.marlow47@quillmail.net) my website (www.DevonMarlow.org) and my License number (BRE:07315942). I do like my team name colors of black and gold
Logo links are attached:
1. https://www.filecrate.net/sh/918kqwz72pavdle/AAF7QmR2HtK4BnYwPzLxUe_KGb?dl=0
2. https://www.filecrate.net/sh/27w5xvn81rbt094/AACKTJMR46DnQ2Wf7RyGs8Vh3b?dl=0
Updates

Target Market(s)

Real Estate Customers

Industry/Entity Type

Real Estate

Contact Information for Business Card

Classy, yet east ro read and understand

Font styles to use
Sans Serif

Requirements
Must have
• Team and brokerage name, and both slogans.
• Black and gold color scheme.
Nice to have
• Bold writing
Should not have
• cluttered feeling

```html
<!DOCTYPE html>
<html lang="en">
<head>
<meta charset="utf-8">
<title>Marlow and Partners – Business Cards</title>
<link rel="stylesheet" href="https://fonts.googleapis.com/css2?family=Montserrat:wght@400;500;600;700&display=swap">
<style>
  :root {
    --bg: #1c1c1c;
    --card-black: #0a0a0a;
    --card-black-soft: #1a1a1a;
    --gold: #efe07a;
    --gold-pale: #fbf6c9;
    --gold-mid: #ece28f;
    --white: #f4f4f4;
    --silver: #d9d9d9;
    --ink: #222222;
  }
  * { margin: 0; padding: 0; box-sizing: border-box; }
  html, body { width: 1200px; height: 1200px; overflow: hidden; }
  body {
    background: var(--bg);
    font-family: "Montserrat", sans-serif;
    position: relative;
  }
  .card {
    position: absolute;
    left: 180px;
    width: 840px;
    height: 480px;
    overflow: hidden;
    background: linear-gradient(135deg, var(--card-black-soft) 0%, var(--card-black) 55%, #151515 100%);
    box-shadow: 0 14px 30px rgba(0,0,0,.55);
  }
  .card--front { top: 90px; }
  .card--back { top: 630px; }
  .card__shapes { position: absolute; inset: 0; width: 100%; height: 100%; }

  .photo {
    position: absolute;
    background: linear-gradient(160deg, #3a3a3a 0%, #262626 55%, #161616 100%);
  }
  .card--front .photo { right: 40px; top: 36px; width: 230px; height: 290px; }
  .card--back .photo { right: 40px; top: 30px; width: 300px; height: 100px; }

  .brand {
    position: absolute;
    display: flex;
    align-items: center;
    gap: 14px;
    color: var(--silver);
    font-weight: 600;
    text-transform: uppercase;
    letter-spacing: 3px;
  }
  .brand__mark { width: 16px; height: 16px; background: var(--silver); flex: none; }
  .card--front .brand { left: 60px; top: 176px; font-size: 28px; }
  .card--back .brand { left: 48px; top: 62px; font-size: 18px; }

  .tagline {
    position: absolute;
    color: var(--gold);
    font-weight: 500;
  }
  .card--front .tagline { left: 60px; top: 282px; font-size: 19px; letter-spacing: 1.2px; }
  .card--back .tagline { left: 48px; top: 190px; font-size: 17px; letter-spacing: 1px; text-transform: uppercase; }

  .rule {
    position: absolute;
    left: 48px; top: 222px;
    width: 740px; height: 2px;
    background: var(--gold);
  }
  .person { position: absolute; right: 52px; top: 148px; text-align: right; }
  .person__name { color: var(--gold); font-weight: 700; font-size: 28px; letter-spacing: 1.5px; }
  .person__role { color: var(--white); font-weight: 500; font-size: 19px; letter-spacing: 1px; margin-top: 2px; }

  .contacts { position: absolute; left: 48px; top: 248px; list-style: none; }
  .contacts li {
    display: flex; align-items: center; gap: 12px;
    color: var(--white); font-size: 18px; letter-spacing: .8px;
    line-height: 30px;
  }
  .contacts svg { width: 14px; height: 14px; flex: none; }
  .contacts strong { font-weight: 700; }

  .license {
    position: absolute;
    left: 400px; top: 408px;
    color: var(--ink);
    font-size: 20px; font-weight: 500; letter-spacing: 1.2px;
  }
  .license b { font-weight: 700; }
</style>
</head>
<body>

<section class="card card--front" aria-label="Card front">
  <svg class="card__shapes" viewBox="0 0 840 480" aria-hidden="true">
    <defs>
      <linearGradient id="bandFront" x1="0" x2="1" y1="0" y2="0">
        <stop offset="0" stop-color="#fbf6c9"/>
        <stop offset="1" stop-color="#ece28f"/>
      </linearGradient>
    </defs>
    <polygon points="0,335 290,335 325,405 0,405" fill="url(#bandFront)"/>
    <polygon points="345,412 840,412 840,452 360,452" fill="#f4f4f4"/>
  </svg>
  <div class="photo" role="img" aria-label="Portrait photo of the team leader"></div>
  <div class="brand"><span class="brand__mark"></span>Marlow and Partners</div>
  <p class="tagline">Welcome to the new way of Real Estate Sales</p>
</section>

<section class="card card--back" aria-label="Card back">
  <svg class="card__shapes" viewBox="0 0 840 480" aria-hidden="true">
    <defs>
      <linearGradient id="bandBack" x1="0" x2="1" y1="0" y2="0">
        <stop offset="0" stop-color="#ece28f"/>
        <stop offset="1" stop-color="#fbf6c9"/>
      </linearGradient>
    </defs>
    <polygon points="0,382 330,382 318,398 0,398" fill="#f4f4f4"/>
    <polygon points="385,390 800,390 800,480 345,480" fill="url(#bandBack)"/>
    <rect x="802" y="300" width="38" height="80" fill="#f4f4f4"/>
  </svg>
  <div class="photo" role="img" aria-label="Group photo of the real estate team"></div>
  <div class="brand"><span class="brand__mark"></span>Harborline Real Estate Group</div>
  <p class="tagline">Ask about our 20 step plan</p>
  <div class="rule"></div>
  <div class="person">
    <p class="person__name">Corin Walsh</p>
    <p class="person__role">Director</p>
  </div>
  <ul class="contacts">
    <li>
      <svg viewBox="0 0 16 16"><path d="M4 1 L6.5 4.5 L5 6.5 Q6.5 9.5 9.5 11 L11.5 9.5 L15 12 L13 15 Q5 14 1 3 Z" fill="#efe07a"/></svg>
      951-284-7310
    </li>
    <li>
      <svg viewBox="0 0 16 16"><rect x="1" y="3" width="14" height="10" fill="none" stroke="#efe07a" stroke-width="1.6"/><path d="M1 3 L8 9 L15 3" fill="none" stroke="#efe07a" stroke-width="1.6"/></svg>
      devon.marlow47@quillmail.net
    </li>
    <li>
      <svg viewBox="0 0 16 16"><circle cx="8" cy="8" r="6.5" fill="none" stroke="#efe07a" stroke-width="1.6"/><path d="M1.5 8 H14.5 M8 1.5 Q4 8 8 14.5 M8 1.5 Q12 8 8 14.5" fill="none" stroke="#efe07a" stroke-width="1.2"/></svg>
      <span>www.<strong>DevonMarlow</strong>.org</span>
    </li>
  </ul>
  <p class="license"><b>License</b> : (BRE:07315942)</p>
</section>

</body>
</html>
```